Stylish Business Card for Modern hair salon

I need a simple business card design using our salon logo and colours that are in the logo. We service clients of all ages but predominantly those in the 18 to 55 age range. We have a young staff and are looking to have a card that will present a modern and clean image that represents who we are. The card should be in black and white same as our logo. Minimal use of other colours is allowed.

Industry/Entity Type

Hair And Beauty

Contact Information for Business Card

The design should have the following information
salon name - Velvet Room Salon
address - 2751 Birchfield Rd.E. Larkfield, North Shore L7P3K2
phone - 905 614-2870
website - velvetroomexample.ca
instagram - velvetroom.salon
twitter - @VelvetRoomSalon

Colors
000000
ffffff
474747

Requirements
Must have
• simple design, salon name, address, phone, website, instagram, twitter info
• Back of card should have the following:
• YOUR NEXT APPOINTMENT
• DATE
• TIME
Nice to have
• simple design, clear to see and read,
• predominantly black and white colour, minimal use of other colours is ok
Should not have
• many colours, various fonts

```html
<!DOCTYPE html>
<html lang="en">
<head>
<meta charset="utf-8">
<title>Velvet Room Salon — Business Card</title>
<link rel="stylesheet" href="https://fonts.googleapis.com/css2?family=Playfair+Display:wght@400;700&family=Open+Sans:wght@400&family=Tinos&display=swap">
<style>
  :root {
    --black: #000000;
    --white: #ffffff;
    --grey: #474747;
    --stage: #2e2e2e;
    --card-light: #e6e6e6;
    --card-dark-top: #1a1a1a;
    --card-dark-bottom: #050505;
    --watermark: #151515;
  }
  * { box-sizing: border-box; margin: 0; padding: 0; }
  html, body { width: 1200px; height: 1092px; overflow: hidden; }
  body {
    background: var(--stage);
    display: flex;
    align-items: center;
    justify-content: center;
    gap: 40px;
  }
  .card {
    width: 540px;
    height: 312px;
    position: relative;
    overflow: hidden;
  }
  /* Front */
  .card-front {
    background: radial-gradient(ellipse at 50% 45%, var(--card-dark-top), var(--card-dark-bottom) 75%);
    display: flex;
    align-items: center;
    justify-content: center;
  }
  .front-watermark {
    position: absolute;
    inset: 0;
    display: flex;
    flex-direction: column;
    align-items: center;
    justify-content: center;
    font-family: "Playfair Display", serif;
    font-weight: 700;
    font-size: 92px;
    line-height: 1;
    color: var(--watermark);
    text-align: center;
  }
  .front-name {
    position: relative;
    font-family: "Playfair Display", serif;
    font-weight: 700;
    font-size: 48px;
    color: var(--white);
    letter-spacing: 1px;
    white-space: nowrap;
  }
  /* Back */
  .card-back {
    background: var(--card-light);
    color: var(--black);
  }
  .back-name {
    position: absolute;
    top: 34px;
    width: 100%;
    text-align: center;
    font-family: "Playfair Display", serif;
    font-weight: 700;
    font-size: 28px;
  }
  .appointment {
    position: absolute;
    top: 106px;
    width: 100%;
    text-align: center;
    font-family: "Tinos", serif;
    font-size: 17px;
    line-height: 1.2;
    text-transform: uppercase;
  }
  .contact-band {
    position: absolute;
    left: 0;
    right: 0;
    top: 210px;
    height: 66px;
    background: var(--grey);
    color: var(--white);
    font-family: "Open Sans", sans-serif;
    font-size: 12.5px;
    display: grid;
    grid-template-columns: 1fr auto;
    grid-template-rows: 1fr 1fr;
    align-items: center;
    padding: 4px 22px;
    column-gap: 20px;
  }
  .contact-row-bottom {
    grid-column: 1 / 3;
    display: flex;
    justify-content: space-between;
  }
  .contact-item { display: flex; align-items: center; gap: 5px; white-space: nowrap; }
  .contact-item svg { width: 11px; height: 11px; flex: none; }
</style>
</head>
<body>
  <section class="card card-front">
    <div class="front-watermark" aria-hidden="true">
      <span>Velvet</span>
      <span>Room</span>
    </div>
    <h1 class="front-name">Velvet Room Salon</h1>
  </section>

  <section class="card card-back">
    <h2 class="back-name">Velvet Room Salon</h2>
    <div class="appointment">
      <p>Your next appointment</p>
      <p>Date: __/__/____</p>
      <p>Time: __________</p>
    </div>
    <div class="contact-band">
      <span class="contact-item">
        <svg viewBox="0 0 12 12"><path d="M6 0.5a3.8 3.8 0 0 0-3.8 3.8C2.2 7.2 6 11.5 6 11.5s3.8-4.3 3.8-7.2A3.8 3.8 0 0 0 6 0.5zm0 5.3a1.5 1.5 0 1 1 0-3 1.5 1.5 0 0 1 0 3z" fill="#fff"/></svg>
        2751 Birchfield Rd.E. Larkfield, North Shore L7P3K2
      </span>
      <span class="contact-item">
        <svg viewBox="0 0 12 12"><circle cx="6" cy="6" r="5.5" fill="#fff"/></svg>
        velvetroomexample.ca
      </span>
      <div class="contact-row-bottom">
        <span class="contact-item">
          <svg viewBox="0 0 12 12"><path d="M3 0.8l1.6 2.6-1 1.2c.6 1.4 1.6 2.4 3 3l1.2-1 2.6 1.6-.6 2c-4.6.2-8.8-4-8.6-8.6z" fill="#fff"/></svg>
          905 614-2870
        </span>
        <span class="contact-item">
          <svg viewBox="0 0 12 12"><rect x="0.5" y="0.5" width="11" height="11" rx="2" fill="#fff"/></svg>
          velvetroom.salon
        </span>
        <span class="contact-item">
          <svg viewBox="0 0 12 12"><rect x="0.5" y="0.5" width="11" height="11" rx="2" fill="#fff"/></svg>
          @VelvetRoomSalon
        </span>
      </div>
    </div>
  </section>
</body>
</html>
```